Wagely Allies Business Card Design

We need a business card designed around our new logo. The business card should be modern in design & should communicate success, confidence, power, sophistication. The target market is young business professionals. This is for a human resource & payroll outsourcing business.

```html
<!DOCTYPE html>
<html lang="en">
<head>
<meta charset="UTF-8">
<title>Wagely Allies Business Card</title>
<link rel="stylesheet" href="https://fonts.googleapis.com/css2?family=Montserrat:wght@400;500;600&display=swap">
<style>
  :root {
    --backdrop: #1b1b1b;
    --card: #262626;
    --card-edge: #303030;
    --mark: #3a3a3a;
    --silver: #d9d9d9;
    --silver-soft: #b8b8b8;
    --divider: #6a6a6a;
  }
  * { margin: 0; padding: 0; box-sizing: border-box; }
  html, body { width: 1200px; height: 900px; overflow: hidden; }
  body {
    background: var(--backdrop);
    font-family: "Montserrat", sans-serif;
    display: flex;
    flex-direction: column;
    align-items: center;
    justify-content: center;
    gap: 40px;
  }
  .card {
    width: 630px;
    height: 360px;
    background: var(--card);
    border: 1px solid var(--card-edge);
    position: relative;
    overflow: hidden;
  }
  .card-front {
    display: flex;
    align-items: center;
    justify-content: center;
  }
  .brand-name {
    color: var(--mark);
    font-weight: 600;
    letter-spacing: 1px;
    line-height: 1;
    white-space: nowrap;
  }
  .card-front .brand-name { font-size: 52px; }
  .card-back {
    display: flex;
    align-items: center;
  }
  .back-brand {
    width: 285px;
    padding: 0 24px;
    display: flex;
    justify-content: center;
  }
  .back-brand .brand-name { font-size: 27px; letter-spacing: 0.5px; }
  .divider {
    width: 1px;
    height: 200px;
    background: var(--divider);
    flex-shrink: 0;
  }
  .details {
    padding-left: 32px;
    color: var(--silver);
  }
  .person-name {
    font-size: 26px;
    font-weight: 500;
    letter-spacing: 2px;
    text-transform: uppercase;
    white-space: nowrap;
  }
  .person-title {
    font-size: 14px;
    color: var(--silver-soft);
    margin-bottom: 18px;
    letter-spacing: 0.5px;
  }
  .address {
    font-size: 14px;
    line-height: 1.5;
    margin-bottom: 12px;
  }
  .contact-list { list-style: none; font-size: 14px; line-height: 1.6; }
  .contact-list li { display: flex; align-items: center; gap: 8px; }
  .contact-list svg { width: 11px; height: 11px; fill: none; stroke: var(--silver-soft); stroke-width: 1.6; }
</style>
</head>
<body>
  <section class="card card-front">
    <span class="brand-name">Wagely Allies Inc</span>
  </section>

  <section class="card card-back">
    <div class="back-brand">
      <span class="brand-name">Wagely Allies Inc</span>
    </div>
    <div class="divider"></div>
    <div class="details">
      <h1 class="person-name">Daniel Harper</h1>
      <p class="person-title">Director</p>
      <p class="address">2190 Linden Ridge Road,<br>Suite B Oakmont, PA 15139</p>
      <ul class="contact-list">
        <li>
          <svg viewBox="0 0 12 12"><path d="M2 1.5 L4 1.5 L5 4 L3.8 5 Q5 7.5 7 8.2 L8 7 L10.5 8 L10.5 10 Q5 10.5 2 4 Z"/></svg>
          412-555-0148
        </li>
        <li>
          <svg viewBox="0 0 12 12"><rect x="1" y="2.5" width="10" height="7"/><path d="M1 2.5 L6 6.5 L11 2.5"/></svg>
          info@wagelyallies.com
        </li>
        <li>
          <svg viewBox="0 0 12 12"><circle cx="6" cy="6" r="4.8"/><path d="M1.2 6 H10.8 M6 1.2 Q3 6 6 10.8 M6 1.2 Q9 6 6 10.8"/></svg>
          www.wagelyallies.com
        </li>
      </ul>
    </div>
  </section>
</body>
</html>
```